Brantley Water Taxi and Transport

Need to redesign our business cards to relay that we do freight logistics and water taxi service. We also work with gov. agencies doing environmental clean up, oil spill response, remote site construction and work with many of the air taxi and helicopter services on Kodiak Island. Out website is www.brantleywatertaxi-example.com to get a better idea of what we do.

Contact Information for Business Card

I have a previous business card but it just has the logo on the front, and a sunset picture on the back with the contact info. It does not relay what we do and what we can help with. I like a simple straight forward design over a busy one.

Colors
3176b5
0455a3
cfdfed

Requirements
Must have
• logo, email, website, phone number

```html
<!DOCTYPE html>
<html lang="en">
<head>
<meta charset="utf-8">
<title>Brantley Water Taxi and Transport – Business Card</title>
<link rel="stylesheet" href="https://fonts.googleapis.com/css2?family=Work+Sans:wght@400;500;600&display=swap">
<style>
  :root {
    --bg: #161616;
    --card: #1f1f20;
    --card-edge: #2a2a2b;
    --brand-blue: #0455a3;
    --mid-blue: #3176b5;
    --sky-blue: #3fb0e6;
    --pale-blue: #cfdfed;
    --ink: #f2f2f2;
  }
  * { box-sizing: border-box; margin: 0; padding: 0; }
  html, body {
    width: 1200px; height: 900px; overflow: hidden;
    background: var(--bg);
    font-family: "Work Sans", Arial, sans-serif;
    color: var(--ink);
  }
  .canvas {
    width: 1200px; height: 900px;
    display: flex; flex-direction: column; align-items: center; justify-content: center;
    gap: 30px;
  }
  .card {
    width: 700px; height: 400px;
    background: var(--card);
    border: 1px solid var(--card-edge);
    position: relative;
    display: flex; align-items: center;
  }
  .card--front { justify-content: center; }
  .brand {
    display: flex; flex-direction: column; align-items: center; gap: 18px;
    flex: none;
  }
  .brand-artwork {
    width: 300px; height: 110px;
    border-radius: 4px;
    background: linear-gradient(160deg, var(--sky-blue) 0%, var(--mid-blue) 65%, var(--brand-blue) 100%);
  }
  .brand-name {
    color: var(--brand-blue);
    font-weight: 600;
    font-size: 26px;
    letter-spacing: 0.5px;
    text-align: center;
    line-height: 1.25;
    white-space: nowrap;
  }
  .card--back { padding: 0 32px; }
  .card--back .brand { width: 266px; gap: 16px; }
  .card--back .brand-artwork { width: 260px; height: 96px; }
  .card--back .brand-name { font-size: 21px; }
  .divider {
    flex: none;
    width: 2px; height: 200px;
    background: var(--brand-blue);
    margin: 0 28px 0 22px;
  }
  .contact { display: flex; flex-direction: column; white-space: nowrap; min-width: 0; }
  .contact-name {
    color: var(--brand-blue);
    font-size: 26px; font-weight: 500;
    letter-spacing: 1.5px; text-transform: uppercase;
  }
  .contact-role { font-size: 16px; margin: 2px 0 16px; }
  .contact-address { font-size: 15px; line-height: 1.45; margin-bottom: 12px; }
  .contact-line {
    display: flex; align-items: center; gap: 9px;
    font-size: 15px; line-height: 1.55;
  }
  .contact-line svg { width: 13px; height: 13px; flex: none; }
</style>
</head>
<body>
<main class="canvas">
  <section class="card card--front">
    <div class="brand">
      <div class="brand-artwork" role="img" aria-label="Logo illustration area: boat on waves below blue mountains and an orange sun"></div>
      <div class="brand-name">Brantley<br>Water Taxi &amp; Transport</div>
    </div>
  </section>

  <section class="card card--back">
    <div class="brand">
      <div class="brand-artwork" role="img" aria-label="Logo illustration area: boat on waves below blue mountains and an orange sun"></div>
      <div class="brand-name">Brantley<br>Water Taxi &amp; Transport</div>
    </div>
    <div class="divider"></div>
    <div class="contact">
      <div class="contact-name">Daniel Harlow</div>
      <div class="contact-role">Director</div>
      <div class="contact-address">417 Harbor Crest Road<br>Anchorage, AK 99501</div>
      <div class="contact-line">
        <svg viewBox="0 0 16 16" aria-hidden="true"><path d="M4 1l3 3-2 2c1 2 3 4 5 5l2-2 3 3-2 2C7 14 2 9 2 3z" fill="var(--brand-blue)"/></svg>
        907-555-0148
      </div>
      <div class="contact-line">
        <svg viewBox="0 0 16 16" aria-hidden="true"><rect x="1.5" y="3.5" width="13" height="9" fill="none" stroke="var(--brand-blue)" stroke-width="1.4"/><path d="M1.5 3.5L8 9l6.5-5.5" fill="none" stroke="var(--brand-blue)" stroke-width="1.4"/></svg>
        brantleywatertaxi@example.com
      </div>
      <div class="contact-line">
        <svg viewBox="0 0 16 16" aria-hidden="true"><circle cx="8" cy="8" r="6.3" fill="none" stroke="var(--brand-blue)" stroke-width="1.4"/><ellipse cx="8" cy="8" rx="2.6" ry="6.3" fill="none" stroke="var(--brand-blue)" stroke-width="1.2"/><path d="M1.7 8h12.6" stroke="var(--brand-blue)" stroke-width="1.2"/></svg>
        www.brantleywatertaxi-example.com
      </div>
    </div>
  </section>
</main>
</body>
</html>
```